Global Expert Network Firm needs business card design

We need business card design for a new company based in Seoul, South Korea called 'Corwell Insight Partners'. We recruit industry experts covering all countries and connect our client and recruited expert by phone, face-to-face meetings and etc. We are a global expert network firm that is focused on delivering high-quality experts to our clients throughout the world. Our clients include multinational corporations, global consulting firms, private equity firms, venture capital firms, asset management companies.
We have made new logo and please find attachment.(Please use new logo)
Target Market(s)
Global Consulting Firms, Investment Firms, Private Equity Firms, Venture Capital Firms.
Industry/Entity Type
Recruitment
Contact Information for Business Card
We need two Languages (English and Korean Version).
The front is Korean and the back is English version.
[The back] [English]
Company Name: Corwell Insight Partners, Inc.
CEO Name: Daniel Park
Address: #507, Hanbit Bldg, 82 Maebongsan-ro, Dobong-gu, Seoul, 01327, Korea
Tel. +82 2 718 4052
Fax. +82 2 864 1097
Mobile. +82 10 7264 8815
Email: daniel@corwellip.com
Web: www.corwellip.com
[The front] [Korean] => Described in same order as English version.
회사명: 코웰인사이트파트너스(주)
대표이사: 박도현
주소: 서울시 도봉구 매봉산로 82 한빛빌딩 507호
Tel. 02 718 4052
Fax. 02 864 1097
Mobile. 010 7264 8815
Web: www.corwellip.com
Look and feel
Each slider illustrates characteristics of the customer's brand and the style your logo design should communicate.

```html
<!DOCTYPE html>
<html lang="ko">
<head>
<meta charset="utf-8">
<title>Corwell Insight Partners — Business Cards</title>
<link rel="stylesheet" href="https://fonts.googleapis.com/css2?family=Noto+Sans+KR:wght@400;500;700&display=swap">
<style>
  :root {
    --backdrop: #e9e6e2;
    --card: #121213;
    --navy: #29306a;
    --rule: #3a4596;
    --icon: #5a69bd;
    --text: #e6e6ea;
    --muted: #a9abb8;
  }
  * { box-sizing: border-box; margin: 0; padding: 0; }
  html, body { width: 1200px; height: 832px; overflow: hidden; }
  body {
    background: var(--backdrop);
    font-family: "Noto Sans KR", sans-serif;
    display: flex;
    flex-direction: column;
    align-items: center;
    justify-content: center;
    gap: 40px;
  }
  .card {
    position: relative;
    width: 640px;
    height: 366px;
    background: var(--card);
    box-shadow: 0 10px 28px rgba(0,0,0,.25);
    overflow: hidden;
  }
  .brand {
    position: absolute;
    left: 34px;
    bottom: 40px;
    width: 270px;
    display: flex;
    align-items: center;
    gap: 14px;
  }
  .brand-square {
    flex: none;
    width: 44px;
    height: 44px;
    background: var(--navy);
  }
  .brand-name {
    font-size: 18px;
    font-weight: 500;
    line-height: 1.3;
    color: var(--text);
  }
  .contact {
    position: absolute;
    left: 322px;
    top: 44px;
    right: 36px;
  }
  .rule { height: 1.5px; background: var(--rule); }
  .rule.short { width: 140px; margin-left: 66px; }
  .rule.long { margin-top: 14px; }
  .person { margin-top: 14px; color: var(--text); }
  .person .name { font-size: 16px; font-weight: 700; letter-spacing: .3px; }
  .person .title { font-size: 11px; color: var(--muted); margin-top: 1px; }
  .details { list-style: none; margin-top: 14px; }
  .details li {
    display: flex;
    align-items: flex-start;
    color: var(--text);
    font-size: 11px;
    line-height: 1.45;
    margin-bottom: 7px;
  }
  .icons {
    flex: none;
    width: 30px;
    display: flex;
    gap: 3px;
    color: var(--icon);
    padding-top: 2px;
  }
  .icons svg { width: 12px; height: 12px; }
  .pair span { display: block; }
  .address { color: var(--muted); font-size: 10.5px; }
</style>
</head>
<body>

<svg width="0" height="0" style="position:absolute" aria-hidden="true">
  <defs>
    <symbol id="i-phone" viewBox="0 0 12 12"><path d="M2.5 1h2l1 3-1.4 1a6 6 0 0 0 2.9 2.9l1-1.4 3 1v2a1 1 0 0 1-1 1A9.5 9.5 0 0 1 1.5 2a1 1 0 0 1 1-1z" fill="currentColor"/></symbol>
    <symbol id="i-mobile" viewBox="0 0 12 12"><rect x="3" y="0.5" width="6" height="11" rx="1.2" fill="none" stroke="currentColor" stroke-width="1.2"/><circle cx="6" cy="9.6" r=".7" fill="currentColor"/></symbol>
    <symbol id="i-mail" viewBox="0 0 12 12"><rect x=".8" y="2.2" width="10.4" height="7.6" fill="none" stroke="currentColor" stroke-width="1.1"/><path d="M.8 2.4 6 6.6l5.2-4.2" fill="none" stroke="currentColor" stroke-width="1.1"/></symbol>
    <symbol id="i-fax" viewBox="0 0 12 12"><rect x="3" y=".8" width="6" height="3.6" fill="none" stroke="currentColor" stroke-width="1.1"/><rect x="1" y="4.4" width="10" height="5" rx=".8" fill="currentColor"/><rect x="3" y="7.6" width="6" height="3.6" fill="#121213" stroke="currentColor" stroke-width="1.1"/></symbol>
    <symbol id="i-globe" viewBox="0 0 12 12"><circle cx="6" cy="6" r="5.2" fill="none" stroke="currentColor" stroke-width="1.1"/><ellipse cx="6" cy="6" rx="2.2" ry="5.2" fill="none" stroke="currentColor" stroke-width="1"/><path d="M.8 6h10.4M1.8 3.4h8.4M1.8 8.6h8.4" stroke="currentColor" stroke-width=".9"/></symbol>
    <symbol id="i-pin" viewBox="0 0 12 12"><path d="M6 .6a4 4 0 0 1 4 4c0 3-4 6.8-4 6.8S2 7.6 2 4.6a4 4 0 0 1 4-4z" fill="currentColor"/><circle cx="6" cy="4.6" r="1.4" fill="#121213"/></symbol>
  </defs>
</svg>

<section class="card card-front" lang="ko">
  <div class="brand">
    <span class="brand-square" aria-hidden="true"></span>
    <p class="brand-name">Corwell Insight Partners</p>
  </div>
  <div class="contact">
    <div class="rule short"></div>
    <div class="person">
      <p class="name">박도현</p>
      <p class="title">대표이사</p>
    </div>
    <div class="rule long"></div>
    <ul class="details">
      <li><span class="icons"><svg><use href="#i-phone"/></svg><svg><use href="#i-mobile"/></svg></span><div class="pair"><span>02 718 4052</span><span>010 7264 8815</span></div></li>
      <li><span class="icons"><svg><use href="#i-mail"/></svg><svg><use href="#i-fax"/></svg></span><div class="pair"><span>daniel@corwellip.com</span><span>02 864 1097</span></div></li>
      <li><span class="icons"><svg><use href="#i-globe"/></svg></span><span>www.corwellip.com</span></li>
      <li><span class="icons"><svg><use href="#i-pin"/></svg></span><span class="address">서울시 도봉구 매봉산로 82<br>한빛빌딩 507호</span></li>
    </ul>
  </div>
</section>

<section class="card card-back" lang="en">
  <div class="brand">
    <span class="brand-square" aria-hidden="true"></span>
    <p class="brand-name">Corwell Insight Partners</p>
  </div>
  <div class="contact">
    <div class="rule short"></div>
    <div class="person">
      <p class="name">Daniel Park</p>
      <p class="title">CEO</p>
    </div>
    <div class="rule long"></div>
    <ul class="details">
      <li><span class="icons"><svg><use href="#i-phone"/></svg><svg><use href="#i-mobile"/></svg></span><div class="pair"><span>+82 2 718 4052</span><span>+82 10 7264 8815</span></div></li>
      <li><span class="icons"><svg><use href="#i-mail"/></svg><svg><use href="#i-fax"/></svg></span><div class="pair"><span>daniel@corwellip.com</span><span>+82 2 864 1097</span></div></li>
      <li><span class="icons"><svg><use href="#i-globe"/></svg></span><span>www.corwellip.com</span></li>
      <li><span class="icons"><svg><use href="#i-pin"/></svg></span><span class="address">#507, Hanbit Bldg, 82 Maebongsan-ro,<br>Dobong-gu, Seoul, 01327, Korea</span></li>
    </ul>
  </div>
</section>

</body>
</html>
```